2 x storefront vinyl request

We are transitioning to a storefront office and need two vinyls for the windows.

First vinyl: Use the Dalton Rivers logo, website (www.daltonriversholdings.example) and leasing office number ((555) 318-4472)

Second vinyl: Maintenance Division & phone number (555) 318-4472

```html
<!DOCTYPE html>
<html lang="en">
<head>
<meta charset="utf-8">
<title>Dalton Rivers Properties – Storefront Vinyls</title>
<link rel="stylesheet" href="https://fonts.googleapis.com/css2?family=Open+Sans:wght@400;700&family=Noto+Serif:wght@400&display=swap">
<style>
  :root {
    --ink: #161616;
    --paper: #ffffff;
    --backdrop: #ffffff;
    --shadow: rgba(0, 0, 0, 0.45);
  }
  * { margin: 0; padding: 0; box-sizing: border-box; }
  html, body {
    width: 1200px;
    height: 885px;
    overflow: hidden;
    background: var(--backdrop);
  }
  .canvas {
    position: relative;
    width: 1200px;
    height: 885px;
  }
  .vinyl {
    position: absolute;
    left: 108px;
    width: 982px;
    height: 318px;
    background: var(--paper);
    box-shadow: 0 12px 34px var(--shadow);
    overflow: hidden;
  }
  .vinyl--office { top: 78px; }
  .vinyl--maintenance { top: 468px; }

  /* Office vinyl */
  .brand {
    position: absolute;
    left: 28px;
    top: 0;
    width: 266px;
    height: 318px;
    display: flex;
    align-items: center;
    gap: 16px;
    font-family: "Open Sans", sans-serif;
    font-weight: 700;
    color: var(--ink);
    font-size: 33px;
    line-height: 1.08;
    letter-spacing: -0.5px;
  }
  .brand__square {
    width: 38px;
    height: 38px;
    background: var(--ink);
    flex: none;
  }
  .web {
    position: absolute;
    left: 302px;
    right: 12px;
    top: 82px;
    text-align: center;
    font-family: "Open Sans", sans-serif;
    color: var(--ink);
  }
  .web__label {
    font-size: 20px;
    font-weight: 400;
    letter-spacing: 3px;
  }
  .web__url {
    margin-top: 4px;
    font-size: 28px;
    font-weight: 700;
    letter-spacing: -0.2px;
    white-space: nowrap;
  }
  .band {
    position: absolute;
    right: 0;
    bottom: 0;
    background: var(--ink);
    color: var(--paper);
    display: flex;
    align-items: center;
    justify-content: center;
  }
  .vinyl--office .band {
    left: 294px;
    height: 141px;
    gap: 6px;
    padding: 0 18px;
  }
  .vinyl--maintenance .band {
    left: 0;
    height: 149px;
    gap: 10px;
    padding-right: 40px;
  }
  .phone-icon { fill: var(--paper); flex: none; }
  .phone-number {
    font-family: "Noto Serif", serif;
    font-weight: 400;
    white-space: nowrap;
    letter-spacing: -1px;
  }
  .vinyl--office .phone-number { font-size: 76px; }
  .vinyl--maintenance .phone-number { font-size: 100px; }

  /* Maintenance vinyl */
  .division {
    position: absolute;
    left: 0;
    right: 0;
    top: 50px;
    text-align: center;
    font-family: "Open Sans", sans-serif;
    font-weight: 700;
    font-size: 68px;
    letter-spacing: -0.5px;
    color: var(--ink);
  }
</style>
</head>
<body>
<main class="canvas">
  <section class="vinyl vinyl--office" aria-label="Leasing office window vinyl">
    <div class="brand">
      <span class="brand__square"></span>
      <span class="brand__name">DALTON<br>RIVERS<br>PROPERTIES</span>
    </div>
    <div class="web">
      <p class="web__label">VISIT OUR WEBSITE:</p>
      <p class="web__url">WWW.DALTONRIVERSHOLDINGS.EXAMPLE</p>
    </div>
    <div class="band">
      <svg class="phone-icon" width="80" height="98" viewBox="0 0 100 120" aria-hidden="true">
        <path d="M22 4 L40 30 Q44 37 38 42 L30 48 Q28 52 31 58 Q44 82 60 96 Q65 100 69 96 L76 88 Q82 83 88 88 L98 104 Q101 110 94 114 L82 119 Q70 122 56 112 Q22 86 6 44 Q0 26 8 12 L14 5 Q18 1 22 4 Z"/>
      </svg>
      <span class="phone-number">(555) 318-4472</span>
    </div>
  </section>

  <section class="vinyl vinyl--maintenance" aria-label="Maintenance division window vinyl">
    <h1 class="division">MAINTENANCE DIVISION</h1>
    <div class="band">
      <svg class="phone-icon" width="90" height="110" viewBox="0 0 100 120" aria-hidden="true">
        <path d="M22 4 L40 30 Q44 37 38 42 L30 48 Q28 52 31 58 Q44 82 60 96 Q65 100 69 96 L76 88 Q82 83 88 88 L98 104 Q101 110 94 114 L82 119 Q70 122 56 112 Q22 86 6 44 Q0 26 8 12 L14 5 Q18 1 22 4 Z"/>
      </svg>
      <span class="phone-number">(555) 318-4472</span>
    </div>
  </section>
</main>
</body>
</html>
```